Wine Label Design

Organization name: Halvern Wine Company

My company is called Halvern Wine Company, I’m a wine importer and wholesaler who distributes wine domestically.

We are about to launch a line of three premium and one sparkling wine that we will wholesale to various retailers, wine stores, and restaurants for re-sale. The wines label will have “Dorian Halvern” I plan on having the labels the same and just changing the varietal as needed. My wine are made from premium grapes and will be marketed as a high end wine. My current label size is 3 1/2" wide by 5" in long and the labels can be on a solid background or transparent.

I would like the first label to be for my Cabernet Sauvignon, California, 2012, 750ML (for the size of the bottle) and ALC 13.8% BY VOL (for the alcohol content).

Colors: I am open to any and all designs that would alter my perception of what will be best!

Further:
Current label is boring and poorly done, so hopefully you designers can come up with something better

Industry/Entity Type

It Company

```html
<!DOCTYPE html>
<html lang="en">
<head>
<meta charset="utf-8">
<title>Dorian Halvern Cabernet Sauvignon Label</title>
<link rel="stylesheet" href="https://fonts.googleapis.com/css2?family=Cinzel:wght@600&family=Arimo:wght@700&family=Tinos&display=swap">
<style>
  :root {
    --backdrop: #d6d3d4;
    --label-black: #141416;
    --label-edge: #2a2a2d;
    --silver: #d9d9db;
    --text-light: #e8e8e8;
    --gold-light: #f6e08a;
    --gold-deep: #b48a2a;
  }
  * { margin: 0; padding: 0; box-sizing: border-box; }
  html, body {
    width: 848px;
    height: 1200px;
    overflow: hidden;
    background: var(--backdrop);
  }
  .canvas {
    position: relative;
    width: 848px;
    height: 1200px;
  }
  .label {
    position: absolute;
    left: 204px;
    top: 90px;
    width: 440px;
    height: 1020px;
    background: var(--label-black);
    border: 2px solid var(--label-edge);
    color: var(--text-light);
    text-align: center;
  }
  .vintage {
    position: absolute;
    top: 64px;
    width: 100%;
    font-family: "Tinos", serif;
    font-size: 34px;
    letter-spacing: 1px;
  }
  .brand-name {
    position: absolute;
    top: 132px;
    width: 100%;
    font-family: "Cinzel", serif;
    font-weight: 600;
    font-size: 64px;
    line-height: 70px;
    letter-spacing: 2px;
    color: var(--silver);
  }
  .emblem-area {
    position: absolute;
    left: 100px;
    top: 318px;
    width: 240px;
    height: 250px;
  }
  .varietal {
    position: absolute;
    top: 706px;
    width: 100%;
    font-family: "Arimo", sans-serif;
    font-weight: 700;
    font-size: 35px;
    line-height: 46px;
    letter-spacing: 1.5px;
  }
  .region {
    position: absolute;
    top: 810px;
    width: 100%;
    font-family: "Tinos", serif;
    font-size: 24px;
    letter-spacing: 2px;
  }
  .volume, .alcohol {
    position: absolute;
    top: 926px;
    font-family: "Tinos", serif;
    font-size: 24px;
  }
  .volume { left: 50px; }
  .alcohol { right: 50px; }
</style>
</head>
<body>
<main class="canvas">
  <section class="label">
    <p class="vintage">2012</p>
    <h1 class="brand-name">DORIAN<br>HALVERN</h1>
    <svg class="emblem-area" viewBox="0 0 240 250" role="img" aria-label="Winery emblem in gold">
      <defs>
        <radialGradient id="gold-glow" cx="50%" cy="50%" r="50%">
          <stop offset="0%" stop-color="var(--gold-light)" stop-opacity="0.55"/>
          <stop offset="100%" stop-color="var(--gold-deep)" stop-opacity="0"/>
        </radialGradient>
      </defs>
      <rect width="240" height="250" fill="url(#gold-glow)"/>
    </svg>
    <h2 class="varietal">CABERNET<br>SAUVIGNON</h2>
    <p class="region">CALIFORNIA</p>
    <p class="volume">750ML</p>
    <p class="alcohol">13.8%ALC</p>
  </section>
</main>
</body>
</html>
```